Flyer Design Project for Wellgrove Mind Clinic

We are a psychology clinic that specialises in eating, parenting and chronic illness & pain. See our website for a summary.

We need a flyer that will go to doctors and schools in the local area.

Things to include on the front page:

Immediate appointments available
After hours appointments available
Male and female psychologists

Phone 9362 5184
Web wellgrovemindclinic.com.au

On the back page:

Phone 9362 5184
Suite 2/1187 Ferntree Rd, Ashbury Vale 3142.
wellgrovemindclinic.com.au

Parenting: Parenthood is an amazing journey, but for lots of people it raises all sorts of issues from fear of birth, breastfeeding difficulties and settling problems, to toddler discipline and food fussiness all the way through to getting help for your depressed or anxious adolescent. Our Parenting Psychologists can help you be the best parent you can be which will in turn lead to happier families, homes, children and parents.

Chronic illness/pain: Diabetes, heart disease, arthritis, asthma, migraines, dizziness, chronic fatigue syndrome, infertility, and PCOS are just some of the conditions that can be managed with psychological interventions. Everything we do is about helping you to manage your condition and get back to focusing on what you really want your life to be about.

Eating: Whether you suffer from anorexia, bulimia or binge eating, our strategies help you develop a healthy relationship with food and your body. The practical tips and strategies that we can provide are very useful for people undergoing lapband surgery or liposuction.

I am interested in whether the photographs that I have already purchased can be used...so please have a look through the website and see which you think will suit your design. Photographs are not absolutely necessary though, so if it doesn't fit with your idea that is okay too.
Updates

HI Everyone,

Thanks for submitting so far! I haven't found anything yet that has hit the mark. And I am thinking that is my fault and maybe that way i have described what I want. I apologise and hope that this update might help.

This brochure is likely to sit with lots of other brochures in a doctors waiting room so it needs to be different - so that it will be noticed.

The majority of our market are women - so something feminine is important. Maybe it needs to be a little more playful that I had initially thought. Like maybe not your standard blocky text and bolds and primary colours. But something more creative, more personal.

I want to not focus just on the family theme. Parenting is one area that we cover, but also we help people with eating disorders and chronic illness/chronic pain. So the photographs that I use need to be more general. It is importnat to focus on happy and healthy looking people. As we went to appeal to what my potential clients want to look like and feel like.

I do hope this helps to guide you. I promise that once I see a flyer that I could choose, I will turn the funding to guaranteed. I did this last time...I am just a bit nervous as I haven't received anything yet that I am excited about.

Kindest regards,

Marietta.

Hi Everyone,

Thank you for your designs coming in! As promised, as soon as I received a design that I could see myself choosing I would change the status from refundable to committed. I have now done this!

I have received a design that I would say is good. It is not perfect however...so please keep the ideas coming.

To give more direction, the one that came in has a nice theme that runs through the brochure. Not too many different types of font and colours detracting from the flow of the flyer. However, the thing that I am concerned about is whether it will stand out enough on a rack of other flyers in a doctors waiting room.

I hope this helps with your creative ideas.

Thanks again to everyone!

Marietta.

Thanks SO much to everyone who is putting in designs. You are making my decision difficult!

I am wondering if you can update your designs with a few things:

can I ask you to make some text changes:

1. Can we have a heading on the front page: Psychologists  and then can you put Ashbury Vale in smaller writing just below it?

2. Id like to say on the front: Specialising in parenting, disordered eating and chronic pain & illness

3. Delete Male & Female Psychologists

4. In general we dont' need to have the logo standing out. We don't have a well known brand yet, so I am not wanting to take up valuable space with this - so perhaps it shoudl be small and maybe just on the back? Keeping the name of our clinic on the front with the website shoudl be sufficient.

Thanks heaps everyone...I will make decision very soon!

Target Market(s)

20-40 year olds. Working. Educated. Female. They might have a family/children.
Australian. Engish speaking.

Industry/Entity Type

Clinic

Requirements
Must have
• I would like to include our logo. Please do not use the colour green that it is in. I hate that colour! but I LOVE the logo.

I would like to follow through with some of the themes of the website and other stationary.

I will attach some of the other stationary I have had designed.

I really like the colours in the letterhead - especially that blue of the logo.

I think it needs to have a dash of colour with it at least...something that will stand out and be noticed on a brochure rack...but also have a look of class/sophistication/modern.
Nice to have
• Perhaps photograph of happy and healthy people.
Should not have
• I don't like bold text or too many different types of fonts.

It shouldn't look too cluttered so I might need to reduce the text I have included - I will need to see it first.

```html
<!DOCTYPE html>
<html lang="en">
<head>
<meta charset="utf-8">
<title>Wellgrove Mind Clinic – Flyer</title>
<link href="https://fonts.googleapis.com/css2?family=Source+Sans+3:wght@400;600&display=swap" rel="stylesheet">
<style>
  :root {
    --backdrop: #7d5a3c;
    --olive: #9b9a79;
    --charcoal: #4a4a48;
    --paper: #e9eaeb;
    --teal: #3f7d79;
    --band: #5fa7a8;
    --ink: #333;
  }
  * { box-sizing: border-box; margin: 0; padding: 0; }
  html, body { width: 1200px; height: 1176px; overflow: hidden; }
  body {
    background: var(--backdrop);
    font-family: "Source Sans 3", "Myriad Pro", sans-serif;
    position: relative;
  }
  .panel {
    position: absolute;
    top: 81px;
    width: 466px;
    height: 987px;
    overflow: hidden;
  }
  .panel--back { left: 111px; background: var(--olive); }
  .panel--front { left: 637px; background: var(--paper); }

  .band { height: 16px; width: 100%; background: var(--band); }

  /* Back page */
  .services {
    height: 611px;
    padding: 38px 33px 0 41px;
    color: #fff;
  }
  .service {
    font-size: 15.2px;
    line-height: 21.6px;
    text-align: justify;
    margin-bottom: 34px;
  }
  .service__title {
    font-size: 28px;
    font-weight: 400;
    line-height: 28px;
    margin-right: 3px;
  }
  .photo { width: 100%; }
  .photo--family {
    height: 225px;
    background: linear-gradient(180deg, #eef1ea 0%, #d9d4c2 45%, #9fb39a 80%, #b6c59a 100%);
  }
  .back-contact {
    background: var(--charcoal);
    height: 119px;
    color: #fff;
    text-align: center;
    padding-top: 24px;
    font-size: 14.5px;
    line-height: 20px;
  }
  .back-contact__web { font-size: 17.5px; margin-top: 9px; }

  /* Front page */
  .photo--picnic {
    height: 309px;
    background: radial-gradient(ellipse at 30% 10%, #eaf2c8 0%, #a9c46e 35%, #6f9a3c 65%, #4d6d2a 100%);
  }
  .clinic-name {
    position: absolute;
    top: 468px;
    left: 0; right: 0;
    text-align: center;
    color: var(--teal);
    font-size: 30px;
    font-weight: 400;
    line-height: 34px;
  }
  .offers {
    position: absolute;
    top: 600px;
    left: 0; right: 0;
    list-style: none;
    text-align: center;
    color: var(--teal);
    font-size: 36px;
    line-height: 39px;
  }
  .offers li { margin-bottom: 24px; }
  .front-contact {
    position: absolute;
    top: 888px;
    left: 0; right: 0;
    text-align: center;
    color: var(--ink);
  }
  .front-contact__phone { font-size: 21px; line-height: 28px; }
  .front-contact__phone strong { font-weight: 600; font-size: 23px; }
  .front-contact__web { font-size: 19px; line-height: 26px; margin-top: 3px; }
  .panel--front .band--bottom { position: absolute; bottom: 0; left: 0; }
</style>
</head>
<body>

<section class="panel panel--back" aria-label="Back page">
  <div class="services">
    <p class="service"><span class="service__title">Parenting:</span> Parenthood is an amazing journey, but for lots of people it raises all sorts of issues from fear of birth, breastfeeding difficulties and settling problems, to toddler discipline and food fussiness all the way through to getting help for your depressed or anxious adolescent. Our Parenting Psychologists can help you be the best parent you can be which will in turn lead to happier families, homes, children and parents.</p>
    <p class="service"><span class="service__title">Chronic illness / pain:</span> Diabetes, heart disease, arthritis, asthma, migraines, dizziness, chronic fatigue syndrome, infertility, and PCOS are just some of the conditions that can be managed with psychological interventions. Everything we do is about helping you to manage your condition and get back to focusing on what you really want your life to be about.</p>
    <p class="service"><span class="service__title">Eating:</span> Whether you suffer from anorexia, bulimia or binge eating, our strategies help you develop a healthy relationship with food and your body. The practical tips and strategies that we can provide are very useful for people undergoing lapband surgery or liposuction.</p>
  </div>
  <div class="band"></div>
  <div class="photo photo--family" role="img" aria-label="Photo of a smiling three-generation family outdoors"></div>
  <div class="band"></div>
  <footer class="back-contact">
    <p>Phone&nbsp; - 9362 5184</p>
    <p>Suite 2/1187 Ferntree Rd, Ashbury Vale 3142.</p>
    <p class="back-contact__web">www.wellgrovemindclinic.com.au</p>
  </footer>
</section>

<section class="panel panel--front" aria-label="Front page">
  <div class="photo photo--picnic" role="img" aria-label="Photo of a mother and toddler on a picnic blanket in a sunny park"></div>
  <div class="band"></div>
  <p class="clinic-name">Wellgrove Mind Clinic</p>
  <ul class="offers">
    <li>Immediate<br>appointments available</li>
    <li>After hours<br>appointments available</li>
    <li>Male and female<br>psychologists</li>
  </ul>
  <div class="front-contact">
    <p class="front-contact__phone">Contact us - <strong>9362 5184</strong></p>
    <p class="front-contact__web">www.wellgrovemindclinic.com.au</p>
  </div>
  <div class="band band--bottom"></div>
</section>

</body>
</html>
```